Steel Company / Iron Railing Business Card Template

We are a custom steel fabrication company located in Harlow Creek, PA. In business since 1979, we recently developed a new logo, and we're looking for a business card design to help display the new logo and our business. The name of the company is Kelbrook Forge Co.. The Office Phone number is (610) 555-0143. We fabricate and install custom "wrought iron" railings on our residential side, we also fabricate and erect structural steel (think cranes and steel beams in buildings) on our commercial side. Looking to get a business card template designed. Something modern, but professional. Clear and easy to read. Front should have all business and employee information including phone number(s), email address, business information, etc. back should spotlight logo.

Industry/Entity Type

Construction / Home Improvement

Contact Information for Business Card

Business information is Kelbrook Forge Co., 48 Dunmore Ave Suite 3305, Harlow Creek, PA 19074. Phone number is (610) 555-0143. Website is www.kelbrookforge.example Business card should be for "Tom Pelling" with the job title "Sales & Estimating" but be editable for other employees. Tom's phone number is (610) 555-0178

Colors

Designer to choose colors to be used in the design.

Requirements
Must have
• Modern Feel, Design should be sized for standard business card sizing 3.5" x 2" (88.9mm x 50.8mm)

```html
<!DOCTYPE html>
<html lang="en">
<head>
<meta charset="utf-8">
<title>Kelbrook Forge Co. — Business Card</title>
<link href="https://fonts.googleapis.com/css2?family=Lato:wght@400;700;900&display=swap" rel="stylesheet">
<style>
  :root {
    --brand-blue: #1f3a93;
    --brand-red: #d8202a;
    --steel-dark: #3e3e3e;
    --steel-light: #e6e6e6;
    --card-white: #ffffff;
    --page-bg: #eeeeee;
  }
  * { box-sizing: border-box; margin: 0; padding: 0; }
  html, body { width: 1200px; height: 900px; overflow: hidden; }
  body {
    background: var(--page-bg);
    font-family: "Lato", Arial, sans-serif;
    display: flex;
    flex-direction: column;
    align-items: center;
    justify-content: center;
    gap: 44px;
  }
  .card {
    position: relative;
    width: 630px;
    height: 360px;
    background: var(--card-white);
    box-shadow: 0 6px 18px rgba(0,0,0,0.18);
    overflow: hidden;
  }
  .card-art { position: absolute; inset: 0; width: 100%; height: 100%; }
  .contact {
    position: absolute;
    left: 40px;
    top: 48px;
    color: var(--brand-blue);
  }
  .person-name { font-weight: 900; font-size: 30px; line-height: 1.05; }
  .person-title { font-weight: 700; font-size: 15px; margin-top: 2px; }
  .person-phone { font-size: 17px; margin-top: 3px; }
  .divider {
    width: 230px;
    height: 8px;
    margin: 16px 0 14px;
    background: repeating-linear-gradient(90deg, var(--steel-dark) 0 14px, var(--steel-light) 22px, var(--steel-dark) 30px);
  }
  .company-name { font-weight: 900; font-size: 27px; line-height: 1.1; }
  .company-line { font-size: 17px; line-height: 1.35; }
  .brand-name {
    position: absolute;
    color: var(--brand-blue);
    font-weight: 900;
    line-height: 1.05;
    text-align: center;
  }
  .card-front .brand-name { right: 22px; top: 148px; width: 170px; font-size: 30px; }
  .card-back .brand-name { right: 40px; top: 132px; width: 200px; font-size: 36px; }
</style>
</head>
<body>

  <section class="card card-front" aria-label="Business card front">
    <svg class="card-art" viewBox="0 0 630 360" aria-hidden="true">
      <defs>
        <linearGradient id="steel-front" x1="0" y1="0" x2="1" y2="1">
          <stop offset="0" stop-color="#4a4a4a"/>
          <stop offset="0.45" stop-color="#f2f2f2"/>
          <stop offset="1" stop-color="#6a6a6a"/>
        </linearGradient>
      </defs>
      <polygon points="390,0 555,0 390,188" fill="url(#steel-front)"/>
      <polygon points="555,0 575,0 390,211 390,188" fill="var(--brand-blue)"/>
      <polygon points="575,0 597,0 390,236 390,211" fill="var(--brand-red)"/>
      <polygon points="630,228 630,248 482,360 456,360" fill="var(--brand-red)"/>
      <polygon points="630,248 630,270 511,360 482,360" fill="var(--brand-blue)"/>
      <polygon points="630,270 630,360 511,360" fill="url(#steel-front)"/>
    </svg>

    <div class="contact">
      <p class="person-name">Tom Pelling</p>
      <p class="person-title">Sales &amp; Estimating</p>
      <p class="person-phone">(610) 555-0178</p>
      <div class="divider"></div>
      <p class="company-name">Kelbrook Forge Co.</p>
      <p class="company-line">48 Dunmore Ave Suite 3305</p>
      <p class="company-line">Harlow Creek, PA 19074</p>
      <p class="company-line">(610) 555-0143</p>
      <p class="company-line">www.kelbrookforge.example</p>
    </div>

    <p class="brand-name">Kelbrook Forge Co.</p>
  </section>

  <section class="card card-back" aria-label="Business card back">
    <svg class="card-art" viewBox="0 0 630 360" aria-hidden="true">
      <defs>
        <linearGradient id="steel-back" x1="0" y1="0" x2="1" y2="0.6">
          <stop offset="0" stop-color="#3a3a3a"/>
          <stop offset="0.5" stop-color="#6e6e6e"/>
          <stop offset="1" stop-color="#3c3c3c"/>
        </linearGradient>
        <linearGradient id="steel-corner" x1="0" y1="0" x2="1" y2="1">
          <stop offset="0" stop-color="#4a4a4a"/>
          <stop offset="0.5" stop-color="#f2f2f2"/>
          <stop offset="1" stop-color="#6a6a6a"/>
        </linearGradient>
      </defs>
      <polygon points="0,0 450,0 130,360 0,360" fill="url(#steel-back)" role="img" aria-label="Brushed dark steel texture"/>
      <polygon points="450,0 478,0 158,360 130,360" fill="var(--brand-blue)"/>
      <polygon points="478,0 506,0 186,360 158,360" fill="var(--brand-red)"/>
      <polygon points="630,228 630,248 482,360 456,360" fill="var(--brand-red)"/>
      <polygon points="630,248 630,270 511,360 482,360" fill="var(--brand-blue)"/>
      <polygon points="630,270 630,360 511,360" fill="url(#steel-corner)"/>
    </svg>

    <p class="brand-name">Kelbrook Forge Co.</p>
  </section>

</body>
</html>
```